Gentle Kundalini Yoga with Gong Relaxation

I teach a gentle Kundalini Yoga class with Gong relaxation every Thursday morning from 8:30-10am at the Ashford Meadows Unity Chapel 17 Garber Lane Pellam Crest. This class is unique in that I play the gong for an extended relaxation. Gongs are generally only found in established Yoga centers not in a small neighborhood yoga class. I am trying to grow this class from a current class size of 5 students. I would like to double the class size.
Updates
Project Deadline Extended
Reason: We had a blizzard on January 27 and 28 in the Boston area and I was too busy removing snow to tend to the postcard design-Thank you-Dora Fitchley
Industry/Entity Type
Church

```html
<!DOCTYPE html>
<html lang="en">
<head>
<meta charset="utf-8">
<title>Gentle Kundalini Yoga with Gong Relaxation – Postcard</title>
<link rel="stylesheet" href="https://fonts.googleapis.com/css2?family=Parisienne&family=Questrial&family=Arimo:wght@700&display=swap">
<style>
  :root {
    --lime: #a9cf3a;
    --orange: #f0922b;
    --ink: #4a4a4a;
    --muted: #5a5a5a;
    --line: #8a8a8a;
    --paper: #ffffff;
    --canvas: #ffffff;
    --pattern: #ececec;
    --pattern-soft: #f6f6f6;
    --skin: #e8c9b4;
  }
  * { margin: 0; padding: 0; box-sizing: border-box; }
  html, body { width: 849px; height: 1200px; overflow: hidden; background: var(--canvas); }
  .sheet { position: relative; width: 849px; height: 1200px; }

  .card {
    position: absolute; left: 65px; width: 724px;
    background: var(--paper); border: 1px solid var(--line); overflow: hidden;
  }
  .card--front { top: 23px; height: 567px; }
  .card--back { top: 607px; height: 536px; }

  .script { font-family: "Parisienne", cursive; color: var(--ink); line-height: 1; }
  .display { font-family: "Questrial", sans-serif; line-height: 1; }
  .info { font-family: "Arimo", Arial, sans-serif; font-weight: 700; color: var(--ink); }

  /* Front */
  .front-pattern {
    position: absolute; left: 40px; top: -40px; width: 430px; height: 430px; border-radius: 50%;
    background: radial-gradient(circle, var(--pattern-soft) 0%, var(--pattern) 60%, var(--paper) 72%);
  }
  .promo-band {
    position: absolute; left: 340px; right: 0; top: 451px; height: 116px; background: var(--lime);
  }
  .front-photo {
    position: absolute; left: 0; top: 0; width: 365px; height: 567px;
    background: linear-gradient(180deg, var(--paper) 0%, #f3ece8 35%, #f6efee 70%, #f2f2f2 100%);
  }
  .front-photo::after {
    content: ""; position: absolute; left: 70px; top: 240px; width: 260px; height: 327px;
    border-radius: 120px 120px 0 0; background: linear-gradient(180deg, #fbe9ec, #f7f3f3);
  }
  .front-title { position: absolute; left: 330px; width: 388px; top: 0; text-align: center; }
  .front-title .script { position: absolute; left: 0; right: 0; top: 110px; font-size: 50px; }
  .front-title .yoga { position: absolute; left: 0; right: 0; top: 150px; font-size: 112px; color: var(--lime); }
  .front-title .with { position: absolute; left: 0; right: 0; top: 255px; font-size: 31px; color: var(--orange); }
  .front-title .gong { position: absolute; left: 0; right: 0; top: 295px; font-size: 34px; color: var(--orange); }
  .tagline {
    position: absolute; left: 330px; width: 388px; top: 368px; text-align: center;
    font-family: "Questrial", sans-serif; font-size: 17px; line-height: 31px; color: var(--muted);
  }
  .cta { position: absolute; left: 340px; right: 0; top: 460px; text-align: center; color: var(--paper); }
  .cta-label { font-family: "Questrial", sans-serif; font-size: 21px; letter-spacing: 0.3px; }
  .cta-phone {
    margin-top: 10px; display: flex; align-items: center; justify-content: center; gap: 10px;
    font-family: "Questrial", sans-serif; font-size: 36px; letter-spacing: 1px;
  }

  /* Back */
  .info-panel {
    position: absolute; left: 0; top: 0; width: 349px; height: 479px;
    background: var(--lime); border-bottom-right-radius: 46px; text-align: center;
  }
  .info-panel .script { position: absolute; left: 0; right: 0; top: 32px; font-size: 44px; }
  .info-panel .yoga { position: absolute; left: 0; right: 0; top: 76px; font-size: 100px; color: var(--paper); }
  .info-panel .with { position: absolute; left: 0; right: 0; top: 166px; font-size: 28px; color: var(--paper); }
  .info-panel .gong { position: absolute; left: 0; right: 0; top: 201px; font-size: 31px; color: var(--paper); }
  .schedule { position: absolute; left: 0; right: 0; top: 262px; }
  .schedule .when { font-size: 22px; line-height: 34px; }
  .schedule .where { font-size: 16px; line-height: 36px; margin-top: 4px; }
  .stamp-box {
    position: absolute; left: 545px; top: 17px; width: 162px; height: 165px; border: 1px solid var(--line);
  }
  .back-pattern {
    position: absolute; left: 470px; top: 210px; width: 300px; height: 330px; border-radius: 50%;
    background: radial-gradient(circle, var(--pattern-soft) 0%, var(--pattern) 55%, var(--paper) 72%);
  }
  .pricing { position: absolute; left: 31px; top: 502px; font-size: 19px; }
</style>
</head>
<body>
<main class="sheet">

  <section class="card card--front" aria-label="Postcard front">
    <div class="front-pattern" role="img" aria-label="Faint grey mandala ornament"></div>
    <div class="promo-band"></div>
    <div class="front-photo" role="img" aria-label="Photograph of a woman meditating cross-legged in a white top"></div>

    <div class="front-title">
      <p class="script">Gentle Kundalini</p>
      <p class="display yoga">YOGA</p>
      <p class="display with">with</p>
      <p class="display gong">Gong Relaxation</p>
    </div>

    <p class="tagline">Immerse yourself in the sound waves<br>of the gong and experience immediate renewal</p>

    <div class="cta">
      <p class="cta-label">JOIN OUR CLASS NOW</p>
      <p class="cta-phone">
        <svg width="38" height="38" viewBox="0 0 38 38" aria-hidden="true">
          <circle cx="19" cy="19" r="17" fill="none" stroke="#ffffff" stroke-width="2.5"/>
          <path d="M13 10c1-1 2.5-1 3 0l2 3.5c.5 1 0 1.8-.7 2.4l-1.2 1c.9 2 2.5 3.7 4.6 4.8l1-1.2c.6-.7 1.5-1 2.4-.5l3.4 2c1 .6 1 2 0 3l-1.6 1.6c-1.4 1.4-4 1-7-1-3.2-2.2-5.8-5.3-7.2-8.6-1.1-2.6-.9-4.8.3-6z" fill="#ffffff"/>
        </svg>
        <span>617-555-0148</span>
      </p>
    </div>
  </section>

  <section class="card card--back" aria-label="Postcard back">
    <div class="back-pattern" role="img" aria-label="Faint grey mandala ornament"></div>
    <div class="stamp-box" aria-label="Stamp area"></div>

    <div class="info-panel">
      <p class="script">Gentle Kundalini</p>
      <p class="display yoga">YOGA</p>
      <p class="display with">with</p>
      <p class="display gong">Gong Relaxation</p>
      <div class="schedule info">
        <p class="when">Every Thursday Morning<br>8:30-10am</p>
        <p class="where">at Ashford Meadows<br>Unity Chapel 17<br>Garber Lane Pellam Crest</p>
      </div>
    </div>

    <p class="pricing info">$12.00/class or a 10 class card for $100.00</p>
  </section>

</main>
</body>
</html>
```